Brindo like IOS/Android app for Okinawa Island - LumaTrail

LumaTrail is the name of the app
The closest thing that I can relate this app to is a region specific Brindo app. The app is for the island of Okinawa and is geared towards English speaking travelers. The style of app that I prefer is a look and feel similar to that of the new Nestora app, color should also be similar if not the same as the nestora app.

The app needs to have the following screens

LOGIN SCREEN
1. App login page with a login for chatterly button or create an account option. Personally I would like an image in the background with a real beachy feel, but don't do this if it messes with your design.

2. Depending on the choice of login there will need to be a second login screen to create the account. Nestora does this nicely.

PRIMARY HOME
primary page similar to the primary layout when you get into the nestora app.
This page is kind of like the home page of the app and should include the following items:
search field
upcoming events
popular things to do
featured restaurants
Featured Places to stay
area guides
Moving here
(this will allow the person to select, housing agencies, auto dealers, schools etc) These are essentially just quick searches.
Each selection should be listed so that the user can swipe to the left or right in order to view more listings under the categories listed above. It will not be the full list but rather a sample.

SIDEBAR POPOUT MENU
Popout sidebar that contains the following selections
Places to Eat
Things to do
Attractions
Beaches
Shop
Farmers Markets
Places to Stay
Schools & DayCare
Housing
Auto
Events
Account settings
Add a business

LIST VIEW
4. List view page for whatever category the user selected. This will show all the listings for the specific category: The top should also have the featured listings for that category

INDIVIDUAL LISTING
5. Listing page
This will include photos, description, hours, map(this can be a button to view the map or the map), Reviews with a leave a review option

AREA GUIDES
6. Area Guides. This is where the user will be able to select a specific area and learn about it. It should include an area where there can be a description, photos with a hero photo image, a map, popular local attractions or things to do, best restaurants in the area, places to stay etc.

PROFILE PAGE
7. Profile page for the user where they can make any updates they need to

Every page but the listing page should include the search bar. When the user clicks in it they should be able to see a drop down of quick select searches or run a regular search.

Logo
I have attached a logo that was made that needs a redesign. The map marker contains the logo for Okinawa within it so it does need to be similar.

If you have any questions or need clarification please send me a message. I will respond promptly.
Thank you,

```html
<!DOCTYPE html>
<html lang="en">
<head>
<meta charset="utf-8">
<title>Account Settings</title>
<link rel="stylesheet" href="https://fonts.googleapis.com/css2?family=Figtree:wght@400;500;600;700&display=swap">
<style>
  :root {
    --page-bg: #f1f1f1;
    --screen-bg: #ffffff;
    --bar-bg: #f8f8f8;
    --accent: #ee5b6b;
    --ink: #222222;
    --ink-soft: #333333;
    --rule: #e4e4e4;
  }
  * { box-sizing: border-box; margin: 0; padding: 0; }
  html, body {
    width: 1200px; height: 1200px; overflow: hidden;
    background: var(--page-bg);
    font-family: "Figtree", "Helvetica Neue", Arial, sans-serif;
    color: var(--ink);
  }
  .screen {
    position: absolute; left: 300px; top: 66px;
    width: 600px; height: 1068px;
    background: var(--screen-bg);
    box-shadow: 0 10px 50px rgba(0,0,0,0.10);
    overflow: hidden;
  }
  .status-bar {
    position: absolute; left: 0; top: 0; width: 100%; height: 34px;
    background: var(--bar-bg);
    font-size: 18px; font-weight: 500;
  }
  .status-bar .signal { position: absolute; left: 10px; top: 7px; display: flex; align-items: center; gap: 5px; }
  .status-bar .time { position: absolute; left: 0; width: 100%; top: 7px; text-align: center; font-weight: 600; }
  .status-bar .battery { position: absolute; right: 10px; top: 7px; display: flex; align-items: center; gap: 6px; }
  .nav-bar {
    position: absolute; left: 0; top: 34px; width: 100%; height: 68px;
    background: linear-gradient(#f8f8f8, #ffffff);
    border-bottom: 1px solid var(--accent);
  }
  .nav-bar .back { position: absolute; left: 27px; top: 24px; }
  .nav-bar .title {
    position: absolute; left: 0; width: 100%; top: 19px; text-align: center;
    font-size: 26px; font-weight: 700; color: var(--ink);
  }
  .nav-bar .logout {
    position: absolute; right: 22px; top: 22px;
    font-size: 21px; font-weight: 500; color: var(--accent);
  }
  .avatar {
    position: absolute; left: 202px; top: 145px; width: 197px; height: 197px;
    border-radius: 50%;
    border: 3px solid #e8e8e8;
    background: linear-gradient(180deg, #b9cfdc 0%, #8a8170 55%, #2b2d2e 100%);
  }
  .profile-name {
    position: absolute; left: 0; width: 100%; top: 364px; text-align: center;
    font-size: 34px; font-weight: 700; color: var(--accent);
  }
  .section-rule { position: absolute; left: 0; top: 445px; width: 100%; height: 1px; background: var(--accent); }
  .details { position: absolute; left: 29px; top: 472px; width: 542px; list-style: none; }
  .detail-row {
    height: 65.5px; border-bottom: 1px solid var(--rule);
    display: flex; align-items: center; font-size: 22px;
  }
  .detail-row .icon { width: 34px; display: flex; align-items: center; }
  .detail-row .label { width: 156px; font-weight: 600; color: var(--ink); }
  .detail-row .value { color: var(--ink-soft); }
  .action-button {
    position: absolute; height: 58px;
    border: 2px solid var(--accent); border-radius: 29px;
    display: flex; align-items: center; justify-content: center; gap: 14px;
    color: var(--accent); font-size: 24px; font-weight: 400;
    background: #fff;
  }
  .edit-profile { left: 186px; top: 742px; width: 228px; }
  .change-password { left: 146px; top: 820px; width: 309px; }
</style>
</head>
<body>
  <main class="screen">
    <div class="status-bar">
      <div class="signal">
        <svg width="56" height="10" viewBox="0 0 56 10">
          <circle cx="5" cy="5" r="4.2" fill="#000"/><circle cx="16" cy="5" r="4.2" fill="#000"/><circle cx="27" cy="5" r="4.2" fill="#000"/>
          <circle cx="38" cy="5" r="3.7" fill="none" stroke="#000" stroke-width="1"/><circle cx="49" cy="5" r="3.7" fill="none" stroke="#000" stroke-width="1"/>
        </svg>
        <span>Carrier</span>
        <svg width="18" height="14" viewBox="0 0 18 14">
          <path d="M1 5 A11 11 0 0 1 17 5" fill="none" stroke="#000" stroke-width="2"/>
          <path d="M4 8 A7 7 0 0 1 14 8" fill="none" stroke="#000" stroke-width="2"/>
          <path d="M9 13 L6.5 10.5 A3.5 3.5 0 0 1 11.5 10.5 Z" fill="#000"/>
        </svg>
      </div>
      <div class="time">4:21 PM</div>
      <div class="battery">
        <svg width="10" height="18" viewBox="0 0 10 18"><path d="M1 5 L9 13 L5 17 L5 1 L9 5 L1 13" fill="none" stroke="#888" stroke-width="1.3"/></svg>
        <span>100%</span>
        <svg width="40" height="16" viewBox="0 0 40 16">
          <rect x="0.5" y="1.5" width="35" height="13" rx="2" fill="none" stroke="#000"/>
          <rect x="2" y="3" width="32" height="10" fill="#000"/>
          <rect x="36.5" y="5.5" width="2.5" height="5" fill="#000"/>
        </svg>
      </div>
    </div>

    <header class="nav-bar">
      <svg class="back" width="30" height="20" viewBox="0 0 30 20">
        <path d="M29 10 H2 M11 1 L2 10 L11 19" fill="none" stroke="var(--accent)" stroke-width="1.8"/>
      </svg>
      <h1 class="title">Account Settings</h1>
      <span class="logout">Logout</span>
    </header>

    <div class="avatar" role="img" aria-label="Profile photo of the user outdoors"></div>
    <h2 class="profile-name">Milo Hartley</h2>
    <div class="section-rule"></div>

    <ul class="details">
      <li class="detail-row">
        <span class="icon"><svg width="22" height="22" viewBox="0 0 22 22"><circle cx="11" cy="6" r="5" fill="var(--accent)"/><path d="M1 21 C1 14 5 12.5 11 12.5 C17 12.5 21 14 21 21 Z" fill="var(--accent)"/></svg></span>
        <span class="label">First Name</span><span class="value">Milo</span>
      </li>
      <li class="detail-row">
        <span class="icon"><svg width="22" height="22" viewBox="0 0 22 22"><circle cx="11" cy="6" r="5" fill="var(--accent)"/><path d="M1 21 C1 14 5 12.5 11 12.5 C17 12.5 21 14 21 21 Z" fill="var(--accent)"/></svg></span>
        <span class="label">Last Name</span><span class="value">Hartley</span>
      </li>
      <li class="detail-row">
        <span class="icon"><svg width="22" height="20" viewBox="0 0 22 20"><path d="M1 7 L11 1 L21 7 V19 H1 Z" fill="var(--accent)"/><path d="M1 7 L11 13 L21 7" fill="none" stroke="#fff" stroke-width="1.6"/><path d="M1 19 L9 12 M21 19 L13 12" stroke="#fff" stroke-width="1.4"/></svg></span>
        <span class="label">Email</span><span class="value">milo@inbox.test</span>
      </li>
    </ul>

    <div class="action-button edit-profile">
      <svg width="28" height="28" viewBox="0 0 28 28">
        <path d="M19 3 L25 9 L10 24 L4 18 Z" fill="var(--accent)"/>
        <path d="M3 19.5 L8.5 25 L1 27 Z" fill="var(--accent)"/>
        <path d="M17 5 L23 11" stroke="#fff" stroke-width="1.6"/>
      </svg>
      <span>Edit Profile</span>
    </div>
    <div class="action-button change-password">
      <svg width="28" height="32" viewBox="0 0 28 32">
        <path d="M7 14 V9 A7 7 0 0 1 21 9 V14" fill="none" stroke="var(--accent)" stroke-width="3"/>
        <rect x="1" y="13" width="26" height="19" rx="3" fill="var(--accent)"/>
        <circle cx="14" cy="23" r="3" fill="#fff"/><circle cx="14" cy="23" r="1.3" fill="var(--accent)"/>
      </svg>
      <span>Change Password</span>
    </div>
  </main>
</body>
</html>
```